Visually Compelling Flyer Design - Orvane Benefits

We are a life insurance company looking to create visually compelling flyers that gain attention of potential buyers and simplify the concept. It should be professional, friendly, approachable in nature. Our logo and several rough drafts are included.
We are looking to refine this look and make it ultra professional, clean and easy to follow. A creative brief with brand guidelines is also included.
FLYER 1 — PAY YOURSELF FIRST
EYEBROW TAG
YOUR COMPANY JUST UPGRADED YOUR BENEFITS
HEADLINE
One small decision. A lifetime of protection.
SUBHEADLINE
Permanent life insurance + long-term care coverage, starting at $1 a day.
EYEBROW TAG
CHOOSE YOUR DAILY INVESTMENT
STAT — TIER 1
$1 / day → $20,000 Life Insurance
STAT — TIER 2 (HERO — make this one biggest/most prominent)
$2 / day → $40,000 Life Insurance
★ Most Popular
STAT — TIER 3
$3 / day → $60,000 Life Insurance
CAPTION
Rate locked at enrollment. Benefit never decreases.
EYEBROW TAG
THREE BENEFITS. ONE POLICY.
SUBHEADLINE
Your money works three ways.
CALLOUT — BENEFIT 1
01 | Cash Value Growth
BODY
Averages 6% annually over the last 50 years — guaranteed never to fall below 3%. Better than any savings account. And if you ever need it, you can borrow against it. It's your money.
CALLOUT — BENEFIT 2
02 | Tax-Free Death Benefit
BODY
From day one, your family is protected. The full benefit is paid tax-free to the person you choose — no waiting period, no exceptions. That's your legacy, preserved.
CALLOUT — BENEFIT 3
03 | Long-Term Care Coverage
BODY
70% of Americans will need long-term care. This plan pays 75% of your benefit — upfront and tax-free — to cover those costs while you're still alive. Your retirement savings stay intact. Your family stays protected.
EYEBROW TAG
ALREADY HAVE LIFE INSURANCE THROUGH WORK?
SUBHEADLINE
That's term. It ends when you need it most.
BODY
Term life insurance is designed for temporary needs — protecting your paycheck, your mortgage, your kids while they're home. When you retire, the house is paid off and your children are grown. Term ends because the need ends.
BODY
But one need never ends: your final expenses and the cost of long-term care. This permanent plan stays with you after retirement — when term coverage is gone and getting new coverage is expensive or impossible.
COMPARISON — LEFT COLUMN HEADER
✕ TERM LIFE
COMPARISON — LEFT COLUMN ITEMS
Gets more expensive with age
Ends at retirement
No cash value
Temporary protection only
COMPARISON — RIGHT COLUMN HEADER
✓ THIS PLAN
COMPARISON — RIGHT COLUMN ITEMS
Rate locked forever at enrollment
Stays with you after retirement
Builds real cash value
Permanent protection for life
EYEBROW TAG
WHAT MAKES THIS DIFFERENT
SUBHEADLINE
Built for you. Stays with you.
CALLOUT
✓ Guaranteed Issued
No medical exams. No questions asked. You qualify.
CALLOUT
✓ Group Rate
Because you work here, you get pricing individuals can't access on their own.
CALLOUT
✓ Rate Locked Forever
Your premium never increases. Your benefit never decreases.
CALLOUT
✓ Portable
Change jobs. Retire. Your policy comes with you at the same rate.
CALLOUT
✓ Family Coverage
Protect your spouse and children under the same plan.
SUBHEADLINE
Protect retirement. Preserve dignity. Plan ahead.
CTA
Be on the lookout for your personalized coverage details.
CAPTION
Brokered by Orvane Benefits · Underwritten by TrelloraLife
FLYER 2 — THE LONG-TERM CARE REALITY
EYEBROW TAG
WHAT MOST PEOPLE DON'T KNOW — BUT SHOULD
HEADLINE
Most Americans are unprepared. You don't have to be.
SUBHEADLINE
The long-term care gap is real — and it affects families like yours.
EYEBROW TAG
THE NUMBERS ARE HARD TO IGNORE
STAT
70%
of Americans age 65 and older will need some form of long-term care during their lifetime.
CAPTION
Source: Pike & Marsden, Review of Elder Welfare and Civic Planning, 2018
STAT
3–4%
of Americans over 50 own a private long-term care insurance policy. The gap between who needs it and who has it is staggering.
CAPTION
Source: Dunn & Solberg, QRT Wellness Wire, 2023
STAT
$700 Billion+
Estimated annual U.S. long-term care cost — and it's growing every year.
CAPTION
Source: Brandt Lowe & Petrasek, Civic Policy Roundtable, 2020
STAT
$470 Billion
The estimated value of unpaid care provided by family members every year. That's the real cost — measured in time, stress, and financial sacrifice.
CAPTION
Source: Lindqvist & Oram, Harborline Institute
STAT
80%
of total long-term care spending goes directly to assist retirees. This isn't a young person's problem. But the time to plan is now.
CAPTION
SUBHEADLINE
Long-term care doesn't just cost money. It costs families.
BODY
When there's no plan in place, the people you love absorb the impact — financially, emotionally, and physically. Retirement savings built over a lifetime can disappear in months. Family members step back from their own lives to provide care. Dignity becomes a daily negotiation.
BODY
This is not inevitable. A small decision today changes the entire outcome.
EYEBROW TAG
THE SOLUTION
HEADLINE
The Pay Yourself First Principle.
BODY
Take the first $1, $2, or $3 you make every day and invest it in a permanent life insurance policy that includes long-term care coverage — underwritten by TrelloraLife, offered through your employer at a group rate, and Guaranteed Issued for everyone.
STAT
$1 / day → $20,000 $2 / day → $40,000 $3 / day → $60,000
BODY
The benefit includes three protections in one: a cash value that grows at an average of 6% annually, a tax-free death benefit for your family, and long-term care coverage that pays 75% of your benefit upfront — tax-free — when you need care most.
SUBHEADLINE
Whether you're single, married, with children or without — there is protection in this plan for you.
HEADLINE
CTA
Look for your personalized offer. Coverage details are coming your way.
CAPTION
COPY RULES FOR DESIGNERS
Headlines are one idea only. Never more than two lines.
Stats stand alone. Never buried in a paragraph.
Body copy maxes at 3 sentences per block. If it's longer, cut it.
The $2/day tier is always the hero. Always.
"Guaranteed Issued" appears on both flyers. It's the most important trust signal.
TrelloraLife is always attributed. Always.
The tagline is: Protect retirement. Preserve dignity. Plan ahead. — Use it verbatim.
Target Market(s)
Average Americans with a family - adults looking for life insurance
Industry/Entity Type
Life Insurance & Financial Retirement

```html
<!DOCTYPE html>
<html lang="en">
<head>
<meta charset="utf-8">
<title>Orvane Benefits – Flyers</title>
<link href="https://fonts.googleapis.com/css2?family=Barlow:wght@400;500;600;700&family=Barlow+Condensed:wght@600;700&display=swap" rel="stylesheet">
<style>
:root{
  --stage:#3c414d;
  --paper:#ffffff;
  --navy:#0b2a86;
  --blue:#0448b8;
  --bright:#0a62d8;
  --cyan:#19b2e3;
  --ink:#1d2542;
  --muted:#4a5270;
  --line:#9aa6c8;
  --grey-head:#e1e3e8;
}
*{box-sizing:border-box;margin:0;padding:0}
html,body{width:1200px;height:851px;overflow:hidden;background:var(--stage)}
body{position:relative;font-family:"Barlow",sans-serif;color:var(--ink)}
.page{position:absolute;top:38px;width:550px;height:775px;background:var(--paper);overflow:hidden}
.page--offer{left:44px}
.page--compare{left:607px}
.abs{position:absolute}
.cond{font-family:"Barlow Condensed",sans-serif}

/* brand */
.brand{position:absolute;display:flex;align-items:center;gap:12px}
.brand__dot{width:58px;height:58px;border-radius:50%;background:var(--cyan)}
.brand__name{font-family:"Barlow",sans-serif;font-weight:700;color:var(--navy);font-size:25px;line-height:25px;letter-spacing:.5px}

/* banners */
.banner{position:absolute;color:#fff;font-family:"Barlow Condensed",sans-serif;font-weight:700;line-height:1.15}
.banner--offer{left:262px;top:0;width:288px;height:98px;background:linear-gradient(90deg,var(--bright),var(--navy));clip-path:polygon(0 0,100% 0,100% 80%,62% 80%,38% 100%,0 80%);padding:16px 0 0 30px;font-size:21px}
.banner--compare{left:224px;top:25px;width:326px;height:60px;background:linear-gradient(90deg,var(--bright),var(--navy));clip-path:polygon(4% 0,100% 0,100% 100%,0 100%);padding:6px 0 0 28px;font-size:21px}

.photo{position:absolute}
.photo--family{left:354px;top:87px;width:196px;height:194px;background:linear-gradient(160deg,#d8c6b4,#9c7d68 55%,#e4dad1);-webkit-mask-image:linear-gradient(90deg,transparent,#000 30%),linear-gradient(0deg,transparent,#000 30%);-webkit-mask-composite:source-in;mask-image:linear-gradient(90deg,transparent,#000 30%);}
.photo--walk{left:0;top:549px;width:550px;height:168px;background:linear-gradient(180deg,#e6ece4 0%,#8fa56a 25%,#6d8b47 60%,#c9d2bf 100%);-webkit-mask-image:linear-gradient(180deg,transparent,#000 18%,#000 80%,transparent)}

.headline{position:absolute;left:36px;top:78px;font-family:"Barlow Condensed",sans-serif;font-weight:700;color:var(--navy);font-size:21px;line-height:24px}
.lede{position:absolute;left:36px;top:122px;font-size:8.5px;line-height:14.5px;color:var(--navy)}
.lede b{color:var(--bright)}
.eyebrow{position:absolute;left:36px;top:151px;font-weight:700;font-size:9.5px;line-height:13.5px;color:var(--navy);width:143px}
.eyebrow::after{content:"";position:absolute;left:61px;right:0;bottom:1px;border-bottom:.6px solid var(--navy)}

/* tiers */
.tier{position:absolute;background:#fff;border-radius:6px;box-shadow:0 3px 10px rgba(20,40,90,.18);text-align:center;display:flex;flex-direction:column;align-items:center;overflow:hidden}
.tier--side{top:194px;width:94px;height:116px;padding-top:7px}
.tier--one{left:86px}.tier--three{left:368px}
.tier__price{color:var(--bright);font-weight:700;font-size:17px;line-height:20px}
.tier__arrow{font-size:11px;line-height:12px;color:var(--navy)}
.tier__amount{color:var(--navy);font-weight:700;font-size:16px;line-height:19px;margin-top:2px}
.tier__label{color:var(--navy);font-weight:600;font-size:9px;line-height:11px}
.tier__foot{margin-top:auto;width:100%;height:31px;border-top:.7px solid #b8c2dc;display:flex;align-items:center;justify-content:center;gap:8px;font-size:6.3px;line-height:7.5px;color:var(--navy);text-align:left}
.tier--hero{left:214px;top:171px;width:120px;height:163px;padding-top:14px}
.tier--hero .tier__price{font-size:16px;line-height:42px}
.tier--hero .tier__price strong{font-size:44px;color:var(--navy);margin-right:3px}
.tier--hero .tier__amount{font-size:21px;line-height:24px}
.tier--hero .tier__label{font-size:12px;line-height:14px;margin-top:2px}
.tier--hero .tier__foot{height:37px;background:var(--navy);color:#fff;font-size:8px;line-height:10px;border:none}
.badge{position:absolute;left:238px;top:160px;width:73px;height:14px;background:var(--cyan);color:#fff;font-size:8px;font-weight:700;text-align:center;line-height:14px;border-radius:2px}
.lock-note{position:absolute;left:393px;top:324px;display:flex;gap:7px;font-size:8.5px;line-height:13px;color:var(--navy)}

/* sections */
.divider{position:absolute;left:37px;width:475px;text-align:center}
.divider::before,.divider::after{content:"";position:absolute;top:6px;width:152px;border-top:.7px solid var(--line)}
.divider::before{left:0}.divider::after{right:0}
.divider h2{font-size:10px;font-weight:700;color:var(--navy);line-height:12px}
.divider p{font-size:8.5px;color:var(--navy);margin-top:3px}
.divider--wide{left:61px;width:427px}
.divider--wide::before,.divider--wide::after{width:123px}

.benefit{position:absolute;left:39px;width:470px}
.benefit__icon{position:absolute;left:0;top:0;width:25px;height:25px;border-radius:50%;background:var(--blue);display:flex;align-items:center;justify-content:center}
.benefit h3{margin-left:47px;font-size:10px;font-weight:700;color:var(--bright);line-height:12px}
.benefit p{margin-left:47px;margin-top:4px;font-size:8.5px;line-height:13.4px;color:var(--ink)}

.feature{position:absolute;top:591px;width:70px;text-align:center;color:var(--navy)}
.feature svg{display:block;margin:0 auto}
.feature h4{font-size:8.5px;font-weight:700;line-height:9.5px;margin-top:8px}
.feature p{font-size:5.6px;line-height:6.4px;color:var(--muted);margin-top:2px}

.cta-band{position:absolute;left:37px;top:687px;width:475px;height:46px;background:linear-gradient(90deg,var(--navy),var(--bright));display:flex;color:#fff;font-weight:700;font-size:9.5px;line-height:12px}
.cta-band__half{flex:1;display:flex;align-items:center;gap:10px;padding-left:45px}
.cta-band__half + .cta-band__half{border-left:.7px solid rgba(255,255,255,.6);padding-left:42px}
.cta-band em{font-style:normal;color:var(--cyan)}
.mail{width:26px;height:26px;border-radius:50%;background:var(--cyan);display:flex;align-items:center;justify-content:center;flex:none}

.footer{position:absolute;top:746px;left:0;width:550px;display:flex;justify-content:center;gap:22px;font-size:8.5px;color:var(--navy);align-items:center}
.footer span{display:flex;align-items:center;gap:6px}

/* compare page */
.term-head{position:absolute;left:0;width:550px;top:87px;text-align:center;font-family:"Barlow Condensed",sans-serif;font-weight:700;font-size:20px;color:#0b8fd6}
.copy{position:absolute;left:61px;width:450px;font-size:8.5px;line-height:15.2px;color:var(--navy)}
.copy b{font-weight:700}
.compare{position:absolute;top:248px;width:184px;height:165px;border:.8px solid #c9cfdd;border-radius:6px;overflow:hidden;background:#fff}
.compare--term{left:62px}.compare--plan{left:303px}
.compare__head{height:27px;display:flex;align-items:center;justify-content:center;gap:10px;font-weight:700;font-size:10px;color:var(--navy)}
.compare--term .compare__head{background:var(--grey-head)}
.compare--plan .compare__head{background:linear-gradient(90deg,var(--cyan),var(--bright));color:#fff}
.compare ul{list-style:none;position:relative}
.compare li{position:absolute;left:16px;width:160px;display:flex;gap:8px;font-size:8.5px;line-height:15px;color:var(--navy)}
.compare li i{font-style:normal;font-weight:700;width:8px;flex:none}
.compare--plan li i{color:var(--bright)}
.vs{position:absolute;left:258px;top:321px;width:34px;height:34px;border-radius:50%;background:var(--navy);color:#fff;font-weight:700;font-size:9px;display:flex;align-items:center;justify-content:center}

.life{position:absolute;top:462px;width:86px;text-align:center;color:var(--navy)}
.life svg{display:block;margin:0 auto}
.life h4{font-size:8.5px;font-weight:700;margin-top:8px;line-height:10px}
.life p{font-size:5.6px;line-height:6.4px;color:var(--muted);margin-top:2px}
.vline{position:absolute;top:466px;height:56px;border-left:.7px solid var(--line)}

.peace{position:absolute;left:62px;top:565px;width:171px;height:130px;border-radius:7px;background:linear-gradient(135deg,var(--navy),var(--bright));color:#fff;padding:16px 10px 0 10px}
.peace h3{position:absolute;left:69px;top:15px;font-size:10px;line-height:15.5px;font-weight:700}
.peace h3 em{font-style:normal;color:var(--cyan)}
.peace p{position:absolute;left:10px;top:83px;width:156px;font-size:8.3px;line-height:13.5px}
</style>
</head>
<body>

<!-- ===== Offer flyer ===== -->
<section class="page page--offer">
  <div class="brand" style="left:35px;top:13px">
    <span class="brand__dot"></span>
    <span class="brand__name">ORVANE<br>BENEFITS</span>
  </div>

  <div class="banner banner--offer">YOUR COMPANY JUST<br>UPGRADED YOUR BENEFITS</div>
  <div class="photo photo--family" role="img" aria-label="Photo of a smiling family of four embracing at home"></div>

  <h1 class="headline">One small decision.<br>A lifetime of protection</h1>
  <p class="lede">Permanent life insurance + long-term care coverage,<br>starting at <b>$1 a day</b>.</p>
  <p class="eyebrow">CHOOSE YOUR DAILY<br>INVESTMENT</p>

  <div class="tier tier--side tier--one">
    <div class="tier__price">$1 / day</div>
    <div class="tier__arrow">→</div>
    <div class="tier__amount">$20,000</div>
    <div class="tier__label">Life Insurance</div>
    <div class="tier__foot">
      <svg width="13" height="15" viewBox="0 0 24 28"><path d="M12 1 2 5v8c0 7 4.5 11.5 10 14 5.5-2.5 10-7 10-14V5z" fill="#0b2a86"/><path d="m7 14 4 4 7-8" stroke="#fff" stroke-width="2.6" fill="none"/></svg>
      <span>Rate locked<br>at enrollment</span>
    </div>
  </div>

  <div class="badge">★ Most Popular</div>
  <div class="tier tier--hero">
    <div class="tier__price"><strong>$2</strong>/ day</div>
    <div class="tier__arrow">→</div>
    <div class="tier__amount">$40,000</div>
    <div class="tier__label">Life Insurance</div>
    <div class="tier__foot">
      <svg width="17" height="20" viewBox="0 0 24 28"><path d="M12 1 2 5v8c0 7 4.5 11.5 10 14 5.5-2.5 10-7 10-14V5z" fill="#fff"/><path d="m7 14 4 4 7-8" stroke="#0b2a86" stroke-width="2.6" fill="none"/></svg>
      <span>Rate locked<br>at enrollment</span>
    </div>
  </div>

  <div class="tier tier--side tier--three">
    <div class="tier__price">$3 / day</div>
    <div class="tier__arrow">→</div>
    <div class="tier__amount">$60,000</div>
    <div class="tier__label">Life Insurance</div>
    <div class="tier__foot">
      <svg width="13" height="15" viewBox="0 0 24 28"><path d="M12 1 2 5v8c0 7 4.5 11.5 10 14 5.5-2.5 10-7 10-14V5z" fill="#0b2a86"/><path d="m7 14 4 4 7-8" stroke="#fff" stroke-width="2.6" fill="none"/></svg>
      <span>Rate locked<br>at enrollment</span>
    </div>
  </div>

  <div class="lock-note">
    <svg width="11" height="15" viewBox="0 0 22 30"><path d="M5 13V8a6 6 0 0 1 12 0v5" stroke="#0b2a86" stroke-width="3" fill="none"/><rect x="1" y="13" width="20" height="16" rx="2" fill="#0b2a86"/><rect x="10" y="18" width="2" height="6" fill="#fff"/></svg>
    <span>Rate locked at enrollment.<br>Benefit never decreases.</span>
  </div>

  <div class="divider" style="top:356px"><h2>THREE BENEFITS. ONE POLICY</h2><p>Your money works three ways.</p></div>

  <div class="benefit" style="top:385px">
    <span class="benefit__icon"><svg width="13" height="12" viewBox="0 0 13 12"><rect x="1" y="7" width="2.2" height="5" fill="#fff"/><rect x="4.6" y="5" width="2.2" height="7" fill="#fff"/><rect x="8.2" y="3" width="2.2" height="9" fill="#fff"/><path d="M1 5 6 1l3 2 3-2" stroke="#fff" stroke-width="1" fill="none"/></svg></span>
    <h3>01 | Cash Value Growth</h3>
    <p>Averages 6% annually over the last 50 years - guaranteed never to fall below 3%. Better than any<br>savings account. Borrow it if your ever need it. It´s your money.</p>
  </div>
  <div class="benefit" style="top:437px">
    <span class="benefit__icon"><svg width="13" height="15" viewBox="0 0 24 28"><path d="M12 2 3 6v7c0 6.5 4 10.5 9 13 5-2.5 9-6.5 9-13V6z" stroke="#fff" stroke-width="2.2" fill="none"/><path d="m7.5 14 3.5 3.5 6.5-7" stroke="#fff" stroke-width="2.4" fill="none"/></svg></span>
    <h3>02 | Tax-Free Death Benefit</h3>
    <p>From day one, your family is protected. The full benefit is paid tax-free to the person you choose -<br>no waiting period, no exceptions. That´s your legacy.</p>
  </div>
  <div class="benefit" style="top:489px">
    <span class="benefit__icon"><svg width="14" height="13" viewBox="0 0 28 26"><path d="M14 12C10 8 6 6 6 3.5S9 0 11 1.5 14 5 14 5s1-2 3-3.5 5 0 5 2S18 8 14 12z" fill="#fff"/><path d="M2 14c3 0 6 3 9 6h6M26 14c-3 0-6 3-9 6" stroke="#fff" stroke-width="2.4" fill="none"/></svg></span>
    <h3>03 | Long-Term Care Coverage</h3>
    <p>70% of Americans will need long - term care. This plan pays 75% of your benefit - upfront and tax -<br>free - while you´re alive. Your retirement stays intact. Your family stays protected.</p>
  </div>

  <div class="divider" style="top:560px"><h2>WHAT MAKES THIS DIFFERENT</h2><p>Built for you. Stays with you.</p></div>

  <div class="feature" style="left:72px">
    <svg width="22" height="26" viewBox="0 0 24 28"><path d="M12 2 3 6v7c0 6.5 4 10.5 9 13 5-2.5 9-6.5 9-13V6z" stroke="#0b2a86" stroke-width="1.8" fill="none"/><path d="m7.5 14 3.5 3.5 6.5-7" stroke="#0b2a86" stroke-width="2" fill="none"/></svg>
    <h4>Guaranteed<br>Issued</h4><p>No medical<br>exams.<br>No questions<br>asked.</p>
  </div>
  <div class="feature" style="left:156px">
    <svg width="28" height="26" viewBox="0 0 30 28"><g stroke="#0b2a86" stroke-width="1.6" fill="none"><circle cx="6" cy="6" r="3"/><circle cx="15" cy="5" r="3"/><circle cx="24" cy="6" r="3"/><path d="M2 20v-6a4 4 0 0 1 8 0v6M11 26V13a4 4 0 0 1 8 0v13M20 20v-6a4 4 0 0 1 8 0v6"/></g></svg>
    <h4>Group<br>Rate</h4><p>Exclusive pricing<br>you can only get<br>through your<br>employer.</p>
  </div>
  <div class="feature" style="left:239px">
    <svg width="22" height="26" viewBox="0 0 22 28"><path d="M5 12V7a6 6 0 0 1 12 0v5" stroke="#0b2a86" stroke-width="1.8" fill="none"/><rect x="2" y="12" width="18" height="14" rx="2" stroke="#0b2a86" stroke-width="1.8" fill="none"/><circle cx="11" cy="18" r="1.8" fill="#0b2a86"/></svg>
    <h4>Rate Locked<br>Forever</h4><p>Your Premium<br>never increases.<br>Your benefit<br>never decreases.</p>
  </div>
  <div class="feature" style="left:323px">
    <svg width="24" height="26" viewBox="0 0 24 26"><rect x="2" y="9" width="20" height="14" rx="2" stroke="#0b2a86" stroke-width="1.8" fill="none"/><path d="M8 9V5h8v4" stroke="#0b2a86" stroke-width="1.8" fill="none"/></svg>
    <h4>Guaranteed<br>Issued</h4><p>No medical<br>exams.<br>No questions<br>asked.</p>
  </div>
  <div class="feature" style="left:406px">
    <svg width="24" height="26" viewBox="0 0 24 26"><circle cx="8" cy="5" r="4" fill="#0b2a86"/><circle cx="17" cy="4" r="3.5" fill="#0b2a86"/><path d="M2 25V13a4 4 0 0 1 4-4h4v16zM13 25V11a3 3 0 0 1 3-3h3a3 3 0 0 1 3 3v14z" fill="#0b2a86"/><circle cx="12" cy="15" r="3" fill="#19b2e3"/><path d="M8 25c0-4 2-6 4-6s4 2 4 6z" fill="#19b2e3"/></svg>
    <h4>Guaranteed<br>Issued</h4><p>No medical<br>exams.<br>No questions<br>asked.</p>
  </div>

  <div class="cta-band">
    <div class="cta-band__half">
      <svg width="26" height="30" viewBox="0 0 24 28"><path d="M12 1 2 5v8c0 7 4.5 11.5 10 14 5.5-2.5 10-7 10-14V5z" fill="#19b2e3"/><path d="M12 5 5 8v5.5c0 5 3 8 7 10 4-2 7-5 7-10V8z" fill="#fff"/><path d="M12 8 8 10v3.5c0 3.5 2 5.5 4 7 2-1.5 4-3.5 4-7V10z" fill="#19b2e3"/></svg>
      <span>Protect retirement.<br><em>Preserve dignity.</em><br>Plan ahead.</span>
    </div>
    <div class="cta-band__half">
      <span class="mail"><svg width="13" height="10" viewBox="0 0 13 10"><rect x=".5" y=".5" width="12" height="9" rx="1" fill="#fff"/><path d="m1 1 5.5 4.5L12 1" stroke="#19b2e3" fill="none"/></svg></span>
      <span>Be on the lookout for<br>your personalized coverage<br>details.</span>
    </div>
  </div>

  <div class="footer">
    <span><svg width="10" height="14" viewBox="0 0 10 14"><path d="M5 0a5 5 0 0 0-5 5c0 4 5 9 5 9s5-5 5-9a5 5 0 0 0-5-5z" fill="#0a62d8"/><circle cx="5" cy="5" r="2" fill="#fff"/></svg>18 Alder Quay Road, Suite 40, Brookhaven</span>
    <span><svg width="13" height="13" viewBox="0 0 24 24"><path d="M6.6 10.8a15 15 0 0 0 6.6 6.6l2.2-2.2a1 1 0 0 1 1-.25 11 11 0 0 0 3.6.6 1 1 0 0 1 1 1V20a1 1 0 0 1-1 1A17 17 0 0 1 3 4a1 1 0 0 1 1-1h3.5a1 1 0 0 1 1 1 11 11 0 0 0 .6 3.6 1 1 0 0 1-.25 1z" fill="#0a62d8"/></svg>+1 555 014 2207</span>
    <span><svg width="12" height="12" viewBox="0 0 24 24"><g stroke="#0a62d8" stroke-width="2" fill="none"><circle cx="12" cy="12" r="10"/><path d="M2 12h20M12 2c3 3 4 6.5 4 10s-1 7-4 10c-3-3-4-6.5-4-10s1-7 4-10z"/></g></svg>www.orvanebenefits.example</span>
  </div>
</section>

<!-- ===== Comparison flyer ===== -->
<section class="page page--compare">
  <div class="brand" style="left:35px;top:26px">
    <span class="brand__dot"></span>
    <span class="brand__name">ORVANE<br>BENEFITS</span>
  </div>
  <div class="banner banner--compare">ALREADY HAVE LIFE<br>INSURANCE THROUGH WORK?</div>

  <h1 class="term-head">That’s term.It ends when you need it most.</h1>

  <p class="copy" style="top:130px">Term life insurance is for temporary needs – protecting your paycheck, mortgage, and kids while they’re home.<br>When you retire, the house is paid off and the kids are grown.<br>Term ends because the need ends.</p>
  <p class="copy" style="top:187px"><b>But one need never ends: final expenses and long - term care.</b><br>This permanent plan stays with you after retirement – when term coverage is gone and getting new coverage is<br>expensive or impossible.</p>

  <div class="compare compare--term">
    <div class="compare__head"><span>X</span><span>TERM LIFE</span></div>
    <ul>
      <li style="top:12px"><i>X</i>Gets more expensive with age.</li>
      <li style="top:42px"><i>X</i>Ends at retirement.</li>
      <li style="top:72px"><i>X</i>No cash value</li>
      <li style="top:100px"><i>X</i>Temporary protection only</li>
    </ul>
  </div>
  <div class="vs">VS.</div>
  <div class="compare compare--plan">
    <div class="compare__head"><span>✓</span><span>THIS PLAN</span></div>
    <ul>
      <li style="top:12px"><i>✓</i>Rate locked forever at<br>enrollment.</li>
      <li style="top:42px"><i>✓</i>Stay with you after retirement.</li>
      <li style="top:72px"><i>✓</i>Build real cash value.</li>
      <li style="top:100px"><i>✓</i>Permanent protection for life.</li>
    </ul>
  </div>

  <div class="divider divider--wide" style="top:441px"><h2>BECAUSE REAL LIFE KEEPS GOING</h2></div>

  <div class="life" style="left:78px">
    <svg width="20" height="20" viewBox="0 0 24 24"><path d="M12 21S3 15 3 8.5A4.5 4.5 0 0 1 12 6a4.5 4.5 0 0 1 9 2.5C21 15 12 21 12 21z" stroke="#0a62d8" stroke-width="1.8" fill="none"/><path d="M12 9v6M9 12h6" stroke="#0a62d8" stroke-width="1.8"/></svg>
    <h4>Health changes</h4><p>Coverage stays<br>with you.</p>
  </div>
  <span class="vline" style="left:172px"></span>
  <div class="life" style="left:181px">
    <svg width="24" height="24" viewBox="0 0 24 24"><circle cx="7" cy="3.5" r="2.5" fill="#0a62d8"/><path d="M4 8h5v7h5v7h-2v-5H5a1 1 0 0 1-1-1zM12 10h10v2H12zM15 12h2v10h-2zM20 12h2v10h-2z" fill="#0a62d8"/></svg>
    <h4>Job changes</h4><p>Your policy goes<br>with you.</p>
  </div>
  <span class="vline" style="left:275px"></span>
  <div class="life" style="left:284px">
    <svg width="26" height="24" viewBox="0 0 26 24"><path d="M1 10a12 9 0 0 1 24 0z" stroke="#0a62d8" stroke-width="1.6" fill="none"/><path d="M13 1v21" stroke="#0a62d8" stroke-width="1.6"/></svg>
    <h4>Retirement</h4><p>Protection<br>never stops.</p>
  </div>
  <span class="vline" style="left:377px"></span>
  <div class="life" style="left:386px">
    <svg width="22" height="24" viewBox="0 0 24 26"><circle cx="8" cy="5" r="4" fill="#0a62d8"/><circle cx="17" cy="4" r="3.5" fill="#0a62d8"/><path d="M2 25V13a4 4 0 0 1 4-4h4v16zM13 25V11a3 3 0 0 1 3-3h3a3 3 0 0 1 3 3v14z" fill="#0a62d8"/><circle cx="12" cy="15" r="3" fill="#19b2e3"/><path d="M8 25c0-4 2-6 4-6s4 2 4 6z" fill="#19b2e3"/></svg>
    <h4>Family grows</h4><p>Coverage that<br>keeps up.</p>
  </div>

  <div class="photo photo--walk" role="img" aria-label="Photo of an older couple walking along a boardwalk through tall marsh grass"></div>

  <div class="peace">
    <svg class="abs" style="left:10px;top:25px" width="40" height="46" viewBox="0 0 24 28"><path d="M12 1 2 5v8c0 7 4.5 11.5 10 14 5.5-2.5 10-7 10-14V5z" fill="#0b2a86"/><path d="M12 4.5 5 7.5v5.5c0 5 3 8.5 7 10.5 4-2 7-5.5 7-10.5V7.5z" stroke="#fff" stroke-width="1.6" fill="none"/></svg>
    <h3>Peace of mind<br>today.<br><em>Security for<br>tomorrow.</em></h3>
    <p>A simple decision now can protect your family, your savings, and your dignity.</p>
  </div>

  <div class="footer">
    <span><svg width="10" height="14" viewBox="0 0 10 14"><path d="M5 0a5 5 0 0 0-5 5c0 4 5 9 5 9s5-5 5-9a5 5 0 0 0-5-5z" fill="#0a62d8"/><circle cx="5" cy="5" r="2" fill="#fff"/></svg>18 Alder Quay Road, Suite 40, Brookhaven</span>
    <span><svg width="13" height="13" viewBox="0 0 24 24"><path d="M6.6 10.8a15 15 0 0 0 6.6 6.6l2.2-2.2a1 1 0 0 1 1-.25 11 11 0 0 0 3.6.6 1 1 0 0 1 1 1V20a1 1 0 0 1-1 1A17 17 0 0 1 3 4a1 1 0 0 1 1-1h3.5a1 1 0 0 1 1 1 11 11 0 0 0 .6 3.6 1 1 0 0 1-.25 1z" fill="#0a62d8"/></svg>+1 555 014 2207</span>
    <span><svg width="12" height="12" viewBox="0 0 24 24"><g stroke="#0a62d8" stroke-width="2" fill="none"><circle cx="12" cy="12" r="10"/><path d="M2 12h20M12 2c3 3 4 6.5 4 10s-1 7-4 10c-3-3-4-6.5-4-10s1-7 4-10z"/></g></svg>www.orvanebenefits.example</span>
  </div>
</section>

</body>
</html>
```